One CD cover and design, either Jazz, Classical, or Original

Dear Friends, I am looking for design and cover material for a CD that will be part of a group of three CDs that need to be slightly related to one another, yet the CDs are completely different: One is unaccompanied trumpet (Porch Songs: Craft of the Lone Thread vol.1), one is a classical recital CD ( A Restless Vesper), and one is a trumpet and piano jazz duo (Warmer Hours). For this contest you choose the one you want. Although this is listed as a single project, I am expecting to purchase three designs for three CDs, and it is likely that I want the winner of this contest to be given the contracts for the other two CDs, which is why this is not listed as 3 contests. You can hear me play on YouTube: search Tobias Ernesto Lindqvar

Target Market(s)

Trumpet, jazz, classical, art music

Industry/Entity Type

Group

Requirements
Must have
• I am thinking of beautiful, artful photos and graphics. VRH CDs. Miro/ Klee type art work like high period Halvorne jazz records of the 1950s and 60s . Open to any images that are artistic and compelling, interesting. The particular relationship between the CDs is open: color, style, motifs, or perhaps a trumpet somewhere in the design. At this moment I am thinking of the unity of the book series by Don Esteban Varga. Open to your creative ideas!

```html
<!DOCTYPE html>
<html lang="en">
<head>
<meta charset="utf-8">
<title>Tobias Ernesto Lindqvar — A Restless Vesper</title>
<link rel="stylesheet" href="https://fonts.googleapis.com/css2?family=Oswald:wght@300;600&display=swap">
<style>
  :root {
    --backdrop: #1c1f29;
    --paper: #f2f0ec;
    --ink: #3a3040;
    --plum-band: #281826;
    --band-text: #f1eef2;
    --paint-blue: #1f5fb8;
    --paint-teal: #2f7f9a;
    --paint-yellow: #f0c43a;
    --paint-red: #e3302a;
    --paint-purple: #6a3566;
    --paint-white: #dfe6ee;
  }
  * { margin: 0; padding: 0; box-sizing: border-box; }
  html, body {
    width: 1200px;
    height: 1114px;
    overflow: hidden;
    background: var(--backdrop);
  }
  .cover {
    position: absolute;
    left: 134px;
    top: 96px;
    width: 936px;
    height: 900px;
    display: flex;
    flex-direction: column;
    background: var(--paper);
  }
  .artist-band {
    height: 156px;
    display: flex;
    align-items: center;
    justify-content: flex-end;
    padding: 0 34px;
    background: var(--paper);
    overflow: hidden;
  }
  .artist-name {
    font-family: "Oswald", sans-serif;
    font-weight: 600;
    font-size: 78px;
    line-height: 1;
    letter-spacing: -1px;
    text-transform: uppercase;
    color: var(--ink);
    white-space: nowrap;
    margin-top: 8px;
  }
  .artwork {
    height: 666px;
    background:
      radial-gradient(ellipse 30% 45% at 20% 55%, var(--paint-blue) 0%, transparent 70%),
      radial-gradient(ellipse 18% 40% at 32% 50%, var(--paint-white) 0%, transparent 70%),
      radial-gradient(ellipse 25% 30% at 48% 55%, var(--paint-teal) 0%, transparent 75%),
      radial-gradient(ellipse 35% 20% at 80% 10%, var(--paint-yellow) 0%, transparent 75%),
      radial-gradient(ellipse 30% 18% at 72% 26%, var(--paint-red) 0%, transparent 75%),
      radial-gradient(ellipse 40% 45% at 80% 75%, var(--paint-purple) 0%, transparent 80%),
      linear-gradient(100deg, var(--paint-blue) 0%, var(--paint-teal) 40%, #5e4a6a 65%, var(--paint-purple) 100%);
  }
  .title-band {
    flex: 1;
    display: flex;
    align-items: center;
    justify-content: flex-end;
    padding: 0 34px;
    background: var(--plum-band);
  }
  .album-title {
    font-family: "Oswald", sans-serif;
    font-weight: 300;
    font-size: 44px;
    line-height: 1;
    letter-spacing: 3px;
    text-transform: uppercase;
    color: var(--band-text);
    white-space: nowrap;
  }
</style>
</head>
<body>
  <main class="cover">
    <header class="artist-band">
      <h1 class="artist-name">Tobias Ernesto Lindqvar</h1>
    </header>
    <div class="artwork" role="img" aria-label="Abstract gestural painting with sweeping brushstrokes of blue, white, yellow, red and purple"></div>
    <footer class="title-band">
      <h2 class="album-title">A Restless Vesper</h2>
    </footer>
  </main>
</body>
</html>
```